Recruitment Site Design

We need a design for the login page, about page, and inner pages of a recruitment site for an oil and gas company. Design should be modern, sleek, professional and colors can be blue, green, white, orange or any other recommended colors.

Please also take into consideration that once the users login, they will need to access a form to fill in their information.

** UPDATE: Kindly provide a design for the inner information page consistent with the outer design. Attached is a picture of the basic structure. ***
Updates

Please provide a design for inner pages as shown in the design brief consistent with the registration page provided. 

Reason: We're extending it to get more inside pages.

Target Market(s)

Professionals looking for a career in the oil and gas industry in the Middle East.

Industry/Entity Type

Oil And Gas

Requirements
Must have
• Sleek design

```html
<!DOCTYPE html>
<html lang="en">
<head>
<meta charset="utf-8">
<title>RigCareers – Oil &amp; Gas Recruitment</title>
<link rel="stylesheet" href="https://fonts.googleapis.com/css2?family=Arimo:wght@400;700&display=swap">
<style>
:root{
  --page-bg:#e9e9ea;
  --top-bg:#dededf;
  --band-blue:#143f96;
  --nav-top:#3f74d6;
  --nav-bottom:#1c4fb3;
  --nav-line:#5f8de0;
  --panel:#ffffff;
  --box-line:#d3d3d3;
  --head-top:#f3f3f3;
  --head-bottom:#d6d6d6;
  --text:#3a3a3a;
  --muted:#555;
  --logo:#3a5db0;
  --red:#e3161b;
  --footer-top:#6e6e6e;
  --footer-bottom:#3d3d3d;
  --photo-light:#8fa8c8;
  --photo-dark:#2f5597;
}
*{box-sizing:border-box;margin:0;padding:0}
html,body{width:1200px;height:944px;overflow:hidden}
body{position:relative;font-family:"Arimo",Arial,sans-serif;color:var(--text);background:var(--page-bg)}
.backdrop-top{position:absolute;left:0;top:0;width:1200px;height:218px;background:linear-gradient(var(--top-bg),#d4d4d5)}
.backdrop-band{position:absolute;left:0;top:218px;width:1200px;height:34px;background:linear-gradient(var(--band-blue),#0f2f78)}
.backdrop-footer{position:absolute;left:0;top:848px;width:1200px;height:96px;background:linear-gradient(var(--footer-top),var(--footer-bottom))}
.utility{position:absolute;left:822px;top:9px;width:216px;height:30px;background:#fff;border-radius:3px;box-shadow:0 1px 3px rgba(0,0,0,.25);display:flex;justify-content:center;align-items:center;gap:10px;font-size:13px}
.utility span.sep{color:#777}
.sheet{position:absolute;left:164px;top:50px;width:876px;height:817px;background:var(--panel);border-radius:7px;box-shadow:0 2px 10px rgba(0,0,0,.35)}
.brand{position:absolute;left:189px;top:78px;font-size:42px;color:var(--logo);letter-spacing:-.5px}
.slogan{position:absolute;left:202px;top:130px;font-size:15px;color:var(--muted)}
.date{position:absolute;right:190px;top:146px;font-size:12px;color:#222}
.nav{position:absolute;left:172px;top:170px;width:857px;height:40px;border-radius:3px;background:linear-gradient(var(--nav-top),var(--nav-bottom));display:flex;align-items:center}
.nav a{color:#fff;text-decoration:none;font-size:12px;padding:0 13px;height:40px;line-height:40px;border-right:1px solid var(--nav-line)}
.search{position:absolute;left:851px;top:176px;width:167px;height:28px;background:#fff;border-radius:4px;font-size:11px;font-style:italic;color:#444;padding:8px 9px}
.search svg{position:absolute;right:6px;top:4px}
.slider{position:absolute;left:172px;top:225px;width:588px;height:255px;background:#fff;border:1px solid var(--box-line);box-shadow:0 12px 14px -8px rgba(0,0,0,.35)}
.slide-photo{position:absolute;left:7px;top:6px;width:572px;height:242px;background:linear-gradient(var(--photo-light),var(--photo-dark))}
.arrow{position:absolute;width:32px;height:38px;background:linear-gradient(#fafafa,#cfcfcf);border:1px solid #bbb;border-radius:4px;display:flex;align-items:center;justify-content:center}
.dots{position:absolute;left:432px;top:490px;display:flex;gap:4px}
.dots span{width:15px;height:15px;border-radius:50%;border:2px solid #888;background:#fff}
.dots span.on{background:var(--red)}
.box{position:absolute;background:#fff;border:1px solid var(--box-line);border-radius:4px}
.sectors{left:172px;top:517px;width:193px;height:183px;list-style:none;font-size:11px;padding-top:2px}
.sectors li{height:26px;line-height:26px;padding-left:24px;border-bottom:1px solid #e2e2e2;position:relative}
.sectors li:last-child{border:0}
.sectors li::before{content:"";position:absolute;left:11px;top:10px;border-left:5px solid #444;border-top:3px solid transparent;border-bottom:3px solid transparent}
.welcome{left:376px;top:517px;width:384px;height:183px;padding:11px 18px}
.welcome h1{font-weight:400;font-size:22px;margin-bottom:14px;color:#333}
.welcome p{font-size:12px;line-height:15px;text-indent:30px;text-align:justify}
.box-head{height:33px;line-height:33px;padding-left:14px;font-size:14px;color:#333;background:linear-gradient(var(--head-top),var(--head-bottom));border-bottom:1px solid #c8c8c8;position:relative}
.toggle{position:absolute;right:12px;top:9px;width:18px;height:16px;background:#555;border-radius:2px}
.toggle::after{content:"";position:absolute;left:5px;top:6px;border-top:5px solid #fff;border-left:4px solid transparent;border-right:4px solid transparent}
.benefits{left:172px;top:714px;width:588px;height:144px;background:#f6f6f6}
.benefit-track{position:absolute;left:45px;top:53px;width:500px;height:76px;background:#fff;border-radius:4px;box-shadow:0 1px 4px rgba(0,0,0,.3);display:flex;justify-content:space-around;padding-top:17px}
.benefit-track p{width:156px;font-size:10.5px;line-height:14px;padding-left:13px;position:relative}
.benefit-track p::before{content:"";position:absolute;left:0;top:3px;width:8px;height:8px;border-radius:50%;background:var(--nav-bottom)}
.side{left:770px;width:258px;background:#f2f2f2}
.members{top:228px;height:122px}
.field{position:absolute;left:13px;width:141px;height:21px;background:#fff;border:1px solid #bbb;border-radius:2px}
.field-label{position:absolute;left:168px;font-size:11px}
.forgot{position:absolute;left:13px;top:101px;font-size:10px;text-decoration:underline}
.btn-red{position:absolute;background:linear-gradient(#f33,#d40f14);color:#fff;font-size:12px;text-align:center;border-radius:3px}
.register{top:357px;height:36px}
.register .box-head{height:34px;line-height:34px;border:0;border-radius:4px}
.jobs{top:400px;height:305px}
.jobs table{width:100%;border-collapse:collapse;font-size:10px}
.jobs td{height:34px;border-bottom:1px solid #ddd;padding-left:8px}
.jobs td.region{width:52px}
.jobs td.pay{text-align:right;padding-right:8px}
.view-all{position:absolute;right:13px;bottom:7px;font-size:10px;color:var(--red);text-decoration:underline}
.newsletter{top:714px;height:148px}
.newsletter p{font-size:10px;line-height:13px;padding:10px 12px 0 13px}
.email{position:absolute;left:10px;top:82px;width:157px;height:26px;background:#fff;border:1px solid #bbb;font-size:11px;padding:6px 8px}
.agree{position:absolute;left:11px;top:124px;font-size:10px;display:flex;gap:6px;align-items:center}
.agree span.check{width:10px;height:10px;border:1px solid #999;background:#fff}
.footer-nav{position:absolute;left:0;top:873px;width:1200px;display:flex;justify-content:center;gap:18px;font-size:11px;color:#fff}
.footer-nav span.sep{color:#ccc}
.copyright{position:absolute;left:0;top:918px;width:1200px;text-align:center;font-size:11px;color:#fff}
</style>
</head>
<body>
<div class="backdrop-top"></div>
<div class="backdrop-band"></div>
<div class="backdrop-footer"></div>

<div class="utility"><span>Login</span><span class="sep">|</span><span>Register</span><span class="sep">|</span><span>Contact Us</span></div>

<div class="sheet"></div>
<div class="brand">RigCareers</div>
<div class="slogan">The slogan of your will be here</div>
<div class="date">Wednesday, 7th November, 2012</div>

<nav class="nav">
  <a>HOME</a><a>ABOUT US</a><a>SEARCH JOBS</a><a>CANDIDATES</a><a>RECRUITERS</a><a>FAQ'S</a><a>BLOGS</a><a>ADVICE</a>
</nav>
<div class="search">Search
  <svg width="24" height="20" viewBox="0 0 24 20"><circle cx="9" cy="8" r="6" fill="none" stroke="#1c4fb3" stroke-width="2.5"/><line x1="13" y1="12" x2="20" y2="18" stroke="#1c4fb3" stroke-width="3"/></svg>
</div>

<div class="slider">
  <div class="slide-photo" role="img" aria-label="Photo of an offshore oil platform at sea"></div>
</div>
<div class="arrow" style="left:180px;top:333px"><svg width="12" height="16"><path d="M10 2 3 8l7 6" fill="none" stroke="#444" stroke-width="3"/></svg></div>
<div class="arrow" style="left:717px;top:333px"><svg width="12" height="16"><path d="M2 2l7 6-7 6" fill="none" stroke="#444" stroke-width="3"/></svg></div>
<div class="dots"><span class="on"></span><span></span><span></span><span></span></div>

<ul class="box sectors">
  <li>Oil Trading</li><li>Shipping &amp; Operations</li><li>Middle &amp; Back Office</li><li>Fuel Sales &amp; Distribution</li><li>Lubricants &amp; Chemicals</li><li>Oil Refining</li><li>Gas &amp; Power</li>
</ul>

<div class="box welcome">
  <h1>Welcome to this site.com</h1>
  <p>Lorem ipsum dolor sit amet, consecteteur adipiscing elit. set diem nonumy in convalis gravida neque. Nulla gravida vestibulum metis a acumsan, aliquam in sagitis ut. Solicitudin sed massa ud enim veniam. Curabitur tempus sem vitae mi vestibulum volutpat malesueda erat vestibulum. Sed aliquam dolor at dolor consequat gravida. Fusce mineque tempus nec fequat sit amet . Tincidunt ut leo. Nam semper omare enim.</p>
</div>

<div class="box benefits">
  <div class="box-head">Benefits for Candidates</div>
  <div class="benefit-track">
    <p>Create a FREE virtual CV and let recruiters find you</p>
    <p>Create a FREE virtual CV and let recruiters find you</p>
    <p>Create a FREE virtual CV and let recruiters find you</p>
  </div>
</div>
<div class="arrow" style="left:184px;top:785px;width:26px"><svg width="12" height="16"><path d="M10 2 3 8l7 6" fill="none" stroke="#444" stroke-width="3"/></svg></div>
<div class="arrow" style="left:722px;top:785px;width:26px"><svg width="12" height="16"><path d="M2 2l7 6-7 6" fill="none" stroke="#444" stroke-width="3"/></svg></div>

<div class="box side members">
  <div class="box-head">MEMBERS AREA &nbsp;- Login<span class="toggle"></span></div>
  <div class="field" style="top:42px"></div><span class="field-label" style="top:46px">Username</span>
  <div class="field" style="top:67px"></div><span class="field-label" style="top:71px">Password</span>
  <span class="forgot">Forgot Your Password?</span>
  <div class="btn-red" style="left:167px;top:93px;width:73px;height:21px;line-height:21px">LOG IN</div>
</div>

<div class="box side register">
  <div class="box-head">Not Member? Register Here<span class="toggle"></span></div>
</div>

<div class="box side jobs">
  <div class="box-head">LATEST JOBS<span class="toggle"></span></div>
  <table>
    <tr><td class="region">Vietnam</td><td>offshore structural engineer</td><td class="pay">negotiable</td></tr>
    <tr><td class="region">UK</td><td>Safety Coach</td><td class="pay">US$95000</td></tr>
    <tr><td class="region">UK</td><td>Senior Process engineer</td><td class="pay"></td></tr>
    <tr><td class="region">Gabon</td><td>NDT Inspector</td><td class="pay">negotiable</td></tr>
    <tr><td class="region">UK</td><td>Estimator O&amp;G</td><td class="pay">Excellent</td></tr>
    <tr><td class="region">UK</td><td>Civil Underground engineer</td><td class="pay">negotiable</td></tr>
    <tr><td class="region">UK</td><td>Safety Coach</td><td class="pay">US$95000</td></tr>
  </table>
  <span class="view-all">View All</span>
</div>

<div class="box side newsletter">
  <div class="box-head">NEWSLETTER<span class="toggle"></span></div>
  <p>If you want receive a news about jobs updtae from this site daily, please enter your email address.</p>
  <div class="email">Your email address</div>
  <div class="btn-red" style="left:174px;top:82px;width:77px;height:26px;line-height:26px;font-size:13px;font-weight:700">SUBMIT</div>
  <div class="agree"><span class="check"></span>by clicking this button, you agree with our terms</div>
</div>

<div class="footer-nav">
  <span>Home</span><span class="sep">|</span><span>About Us</span><span class="sep">|</span><span>Search Jobs</span><span class="sep">|</span><span>Candidates</span><span class="sep">|</span><span>Recuiters</span><span class="sep">|</span><span>FAQ's</span><span class="sep">|</span><span>Blogs</span><span class="sep">|</span><span>Log in</span><span class="sep">|</span><span>Register</span><span class="sep">|</span><span>Terms of Use</span><span class="sep">|</span><span>Privacy Policy</span><span class="sep">|</span><span>Contact Us</span>
</div>
<div class="copyright">Copyright &copy; 2012, rigcareers-jobs.com. All rights reserved.</div>
</body>
</html>
```